DM - management consultant

Business card - contemporary design

Front info
Dorian Maples

(Address not necessary)
PO Box 7386
Belmont, CA 94002

(650) 555-0143
dm@dorianmapl.es

Twitter: dmq527
Facebook: /Dorian.Maples
Linkedin: /in/dorianmaples

Back or Front
www.dorianmaples.net
Facilitation & coaching, change management, strategic partnerships, business improvement

Target Market(s)

High tech businesses - mostly startups in Silicon Valley

Industry/Entity Type

Business

Font styles to use
Sans Serif

Colors

Designer to choose colors to be used in the design.

```html
<!DOCTYPE html>
<html lang="en">
<head>
<meta charset="utf-8">
<title>DM – Management Consultant business card</title>
<link rel="stylesheet" href="https://fonts.googleapis.com/css2?family=Source+Sans+3:wght@400;600;700&display=swap">
<style>
  :root {
    --stage-light: #f4f4f5;
    --stage-dark: #c3c4c6;
    --card-white: #ffffff;
    --card-fade: #ececed;
    --ink: #111111;
    --black: #000000;
    --brand-blue: #0f66b0;
    --mark-pale: #d5dfe7;
    --mark-grey: #8a8d93;
    --pattern-dark: #30343c;
    --pattern-mid: #4a4e58;
    --white: #ffffff;
    --accent-red: #d9262c;
  }
  * { margin: 0; padding: 0; box-sizing: border-box; }
  html, body { width: 1200px; height: 1200px; overflow: hidden; }
  body {
    position: relative;
    font-family: "Source Sans 3", "Myriad Pro", Arial, sans-serif;
    background: radial-gradient(circle at 50% 50%, var(--stage-light) 0%, var(--stage-dark) 100%);
  }

  .card {
    position: absolute;
    left: 228px;
    width: 742px;
    box-shadow: 0 2px 6px rgba(0,0,0,0.18);
    overflow: hidden;
  }

  /* Front */
  .card-front { top: 166px; height: 422px; }
  .front-top {
    position: absolute; inset: 0 0 125px 0;
    background: linear-gradient(180deg, var(--card-white) 0%, var(--card-fade) 100%);
    text-align: center;
  }
  .front-mark {
    position: absolute; top: 46px; left: 0; right: 0;
    display: flex; justify-content: center; align-items: center; gap: 14px;
  }
  .mark-square { width: 24px; height: 24px; background: var(--mark-grey); border-radius: 4px; }
  .mark-name {
    font-weight: 700; font-size: 84px; line-height: 1; letter-spacing: -2px; color: var(--ink);
  }
  .holder-name {
    position: absolute; top: 160px; left: 0; right: 0;
    font-weight: 700; font-size: 27px; color: var(--ink);
  }
  .services {
    position: absolute; top: 206px; left: 0; right: 0;
    font-size: 19.5px; line-height: 22px; color: var(--brand-blue);
  }
  .front-band {
    position: absolute; left: 0; right: 0; bottom: 0; height: 125px;
    background: var(--black);
  }
  .band-pattern {
    position: absolute; left: 0; top: 0; width: 322px; height: 125px;
    background: linear-gradient(90deg, var(--pattern-mid) 0%, var(--pattern-dark) 100%);
  }
  .contact {
    position: absolute; left: 462px; top: 20px;
    list-style: none; color: var(--white); font-size: 18.5px; line-height: 27px;
  }

  /* Back */
  .card-back { top: 596px; height: 424px; background: var(--black); }
  .back-mark {
    position: absolute; right: 32px; top: 94px;
    display: flex; align-items: center; gap: 22px;
  }
  .back-mark .mark-square { width: 44px; height: 44px; background: var(--mark-pale); border-radius: 7px; }
  .back-mark .mark-name { font-size: 178px; letter-spacing: -4px; color: var(--mark-pale); }
  .role {
    position: absolute; left: 27px; right: 27px; top: 232px;
    font-weight: 600; font-size: 55px; line-height: 1; color: var(--brand-blue);
    letter-spacing: -0.3px; text-align: center;
  }
  .back-web {
    position: absolute; left: 0; right: 0; top: 380px;
    display: flex; justify-content: center; align-items: center; gap: 6px;
    color: var(--white); font-size: 18.5px;
  }
  .back-web svg { width: 22px; height: 22px; }
</style>
</head>
<body>

<section class="card card-front">
  <div class="front-top">
    <div class="front-mark">
      <span class="mark-square"></span>
      <span class="mark-name">DM</span>
    </div>
    <h1 class="holder-name">Dorian Maples</h1>
    <p class="services">Facilitation &amp; coaching, Change management<br>Strategic partnerships, Business improvement</p>
  </div>
  <div class="front-band">
    <div class="band-pattern" role="img" aria-label="Decorative pattern of rounded grey squares"></div>
    <ul class="contact">
      <li>Phone: (650) 555-0143</li>
      <li>Linkedin: /in/dorianmaples</li>
      <li>www.dorianmaples.net</li>
    </ul>
  </div>
</section>

<section class="card card-back">
  <div class="back-mark">
    <span class="mark-square"></span>
    <span class="mark-name">DM</span>
  </div>
  <p class="role">Management Consultant</p>
  <p class="back-web">
    <svg viewBox="0 0 22 22" aria-hidden="true">
      <circle cx="11" cy="11" r="10" fill="var(--white)"/>
      <circle cx="11" cy="11" r="8" fill="var(--accent-red)"/>
      <g fill="none" stroke="var(--white)" stroke-width="1">
        <ellipse cx="11" cy="11" rx="3.5" ry="8"/>
        <line x1="3" y1="11" x2="19" y2="11"/>
        <line x1="4.5" y1="7" x2="17.5" y2="7"/>
        <line x1="4.5" y1="15" x2="17.5" y2="15"/>
      </g>
    </svg>
    www.dorianmaples.net
  </p>
</section>

</body>
</html>
```